I need a book cover for an Brindle PQS book.
Book size: 6x9in (15.24x22.86cm)
Title: Master ZRT in four weeks.
Place of the title
The title should be at the top and centered as below:
Learn
ZRT
in one month
Below the text I want a cloud with a calendar.
At the bottom of the front page I want a my name below with some effects like i the picture book1
Lucien DE WOLFRANT
Slice of the book should be blue with text
Master ZRT in four weeks L.De Wolfrant
The front part should looks like in the picture attached.
For the back part I want as below:
Color white like the front part
At the top I want this text
About the book (in bold)
ZRT aka Pavlo Merit Syntax is a powerful tool and language used in a lot of solution to write queries in Nimbra Record Viewer, Nimbra Watchpost, Nimbra Lookout, Quellan Bulwark…
It helps you to explore data, identify anomalies, create powerful workbook and reports.
You can use ZRT with Fleetwise to explore things from your devices as well as with Lookout or others to look for security breach.
If you want to start with ZRT, this book is for you and goal is to Master ZRT in four weeks or 30 days.
Every day you will have some exercises to do with key words to do your own research on the web. You will then find the solution and explanation.
At the end of the book we will create a workbook from scratch and give it a cool design.
A bit below I want my picture beside the bio below
Lucien De Wolfrant is a French Modern Workplace consultant and Quellan Star Fellow working at Borvane and living in Paris.
He likes to play with TermaDrive, GLT, Fleetwise, Lattice Hub, ZRT, Trace Insights and all things relating to automation.
You can follow him on his blog (rollgrid-notes.example) or Chirpline (@roll_grid_notes).
A bit below I want a man sit down on a desk with a laptop and looking at a cloud.
There are some data flying from the cloud picture.
The man looks like as in the picture man.jpg and should wear a plaid shirt red and black and no glasses.
i have some other things to modify

```html
<!DOCTYPE html>
<html lang="en">
<head>
<meta charset="utf-8">
<title>Master ZRT in four weeks – Book Cover Wrap</title>
<link href="https://fonts.googleapis.com/css2?family=Archivo:wght@700&family=Archivo+Black&family=Raleway:wght@400&family=Questrial&display=swap" rel="stylesheet">
<style>
  :root {
    --backdrop: #d3d3d3;
    --paper: #ffffff;
    --brand-blue: #4a6db8;
    --spine-blue: #5a7fc2;
    --title-red: #e0203f;
    --text-blue: #4f74bd;
    --white: #ffffff;
    --cloud-light: #c9d8f4;
    --cloud-mid: #8fb0e6;
    --cloud-deep: #5b83d4;
  }
  * { margin: 0; padding: 0; box-sizing: border-box; }
  html, body {
    width: 849px; height: 1200px; overflow: hidden;
    background: var(--backdrop);
  }
  .cover-wrap {
    position: absolute; left: 19.5px; top: 319.5px;
    width: 810px; height: 561px;
    background: var(--paper);
    box-shadow: 4px 5px 8px rgba(0,0,0,0.25);
  }

  /* Back cover */
  .back-cover { position: absolute; left: 0; top: 0; width: 374px; height: 561px; }
  .about-heading {
    position: absolute; left: 42px; top: 27px;
    font-family: "Archivo Black", sans-serif; font-size: 14px;
    color: var(--brand-blue);
  }
  .about-text {
    position: absolute; left: 42px; top: 60px; width: 288px;
    font-family: "Raleway", sans-serif; font-size: 8.2px; line-height: 13px;
    color: var(--text-blue); text-align: justify;
  }
  .about-text p + p { margin-top: 13px; }
  .author-bio {
    position: absolute; left: 42px; top: 243px; width: 288px; height: 121px;
    background: var(--spine-blue);
    border-radius: 14px 24px 24px 0;
    overflow: hidden;
  }
  .author-photo {
    position: absolute; left: 0; top: 4px; width: 76px; height: 117px;
    background: linear-gradient(160deg, #d9d9d9 0%, #8a8a8a 60%, #3c3c3c 100%);
  }
  .bio-text {
    position: absolute; left: 82px; top: 5px; width: 200px;
    font-family: "Raleway", sans-serif; font-size: 7.3px; line-height: 11.6px;
    color: var(--white);
    overflow-wrap: anywhere;
  }
  .bio-text p + p { margin-top: 5px; }
  .desk-scene {
    position: absolute; left: 42px; top: 375px; width: 296px; height: 167px;
    background: radial-gradient(ellipse at 30% 55%, var(--cloud-mid) 0%, var(--cloud-light) 45%, rgba(255,255,255,0) 75%);
  }

  /* Spine */
  .spine {
    position: absolute; left: 374px; top: 0; width: 61px; height: 561px;
    background: var(--spine-blue); color: var(--white);
  }
  .spine-title {
    position: absolute; left: 10px; top: 26px;
    writing-mode: vertical-rl;
    font-family: "Archivo", sans-serif; font-weight: 700; font-size: 11.5px;
    letter-spacing: 0.5px; white-space: nowrap;
  }
  .spine-title .spine-key {
    font-family: "Archivo Black", sans-serif; font-size: 25px; line-height: 25px;
    margin: 2px 0;
  }
  .spine-author {
    position: absolute; left: 18px; top: 300px;
    writing-mode: vertical-rl;
    font-family: "Questrial", sans-serif; font-size: 19px; letter-spacing: 1px;
    border-left: 1.2px solid var(--white); padding-left: 1px;
    white-space: nowrap;
  }

  /* Front cover */
  .front-cover { position: absolute; left: 435px; top: 0; width: 375px; height: 561px; }
  .title { position: absolute; left: 0; top: 20px; width: 375px; text-align: center; }
  .title-top {
    display: block; font-family: "Archivo", sans-serif; font-weight: 700;
    font-size: 44px; line-height: 50px; color: var(--brand-blue);
  }
  .title-key {
    display: block; font-family: "Archivo Black", sans-serif;
    font-size: 124px; line-height: 118px; color: var(--title-red);
    text-shadow: 2px 3px 3px rgba(0,0,0,0.3);
  }
  .title-bottom {
    display: block; font-family: "Archivo", sans-serif; font-weight: 700;
    font-size: 35px; line-height: 44px; color: var(--brand-blue);
  }
  .cloud-calendar {
    position: absolute; left: 32px; top: 250px; width: 314px; height: 248px;
    background: radial-gradient(ellipse at 50% 55%, var(--cloud-deep) 0%, var(--cloud-mid) 40%, var(--cloud-light) 62%, rgba(255,255,255,0) 78%);
  }
  .front-author {
    position: absolute; left: 0; top: 510px; width: 375px; text-align: center;
    font-family: "Questrial", sans-serif; font-size: 20px; letter-spacing: 1px;
    color: var(--brand-blue);
  }
  .front-author span { border-bottom: 1.3px solid var(--brand-blue); padding-bottom: 1px; }
</style>
</head>
<body>
  <main class="cover-wrap">
    <section class="back-cover">
      <h2 class="about-heading">About the book</h2>
      <div class="about-text">
        <p>ZRT aka Pavlo Merit Syntax is a powerful tool and language used in a lot of solution to write queries in Nimbra Record Viewer, Nimbra Watchpost, Nimbra Lookout, Quellan Bulwark…</p>
        <p>It helps you to explore data, identify anomalies, create powerful workbook and reports. You can use ZRT with Fleetwise to explore things from your devices as well as with Lookout or others to look for security breach.</p>
        <p>If you want to start with ZRT, this book is for you and goal is to Master ZRT in four weeks or 30 days. Every day you will have some exercises to do with key words to do your own research on the web. You will then find the solution and explanation. At the end of the book we will create a workbook from scratch and give it a cool design.</p>
      </div>
      <div class="author-bio">
        <div class="author-photo" role="img" aria-label="Black and white portrait photo of the author"></div>
        <div class="bio-text">
          <p>Lucien De Wolfrant is a French Modern Workplace consultant and Quellan Star Fellow working at Borvane and living in Paris.</p>
          <p>He likes to play with TermaDrive, GLT, Fleetwise, Lattice Hub, ZRT, Trace Insights and all things relating to automation.</p>
          <p>You can follow him on his blog (rollgrid-notes.example) or Chirpline (@roll_grid_notes).</p>
        </div>
      </div>
      <div class="desk-scene" role="img" aria-label="Illustration of a man at a desk with a laptop in front of a blue cloud, with binary digits flying out"></div>
    </section>

    <aside class="spine">
      <div class="spine-title">MASTER <span class="spine-key">ZRT</span> IN FOUR WEEKS</div>
      <div class="spine-author">Lucien DE WOLFRANT</div>
    </aside>

    <section class="front-cover">
      <h1 class="title">
        <span class="title-top">MASTER</span>
        <span class="title-key">ZRT</span>
        <span class="title-bottom">IN FOUR WEEKS</span>
      </h1>
      <div class="cloud-calendar" role="img" aria-label="3D illustration of a blue cloud with a calendar page showing the number 1"></div>
      <p class="front-author"><span>Lucien DE WOLFRANT</span></p>
    </section>
  </main>
</body>
</html>
```